Brindle Offers is an online marketing platform.

A daily deals site for consumers a way to bring in new clients for clients and this is who the business cards are for. Industries - Food and Drink, Things To Do, Beauty and Spas, Staycations and Services.
Logo on one side.
Name - Owen Radley
Job Title - Sales Director
Phone Number - 07912358046
Email - owen@brindleoffers.co.uk
need same for second person
Name - Fiona Bracken
Job Title - Operations Director
Phone Number - 01632840275
Email - fiona@brindleoffers.co.uk
Bottom Right - Chatterbook Icon, Snapa Icon, Pipline Icon
Target Market(s)
Business owners of the above industries
Contact Information for Business Card
Name - Owen Radley
Name - Fiona Bracken
Look and feel

```html
<!DOCTYPE html>
<html lang="en">
<head>
<meta charset="utf-8">
<title>Brindle Offers — Business Cards</title>
<link rel="stylesheet" href="https://fonts.googleapis.com/css2?family=Lato:wght@400;700&family=Roboto:wght@300;400&display=swap">
<style>
  :root {
    --brand-blue: #0f5aa8;
    --brand-grey: #6d6e70;
    --text-grey: #4a4a4a;
    --title-grey: #7a7a7a;
    --card-white: #ffffff;
    --backdrop: #3b3b3b;
    --chatterbook: #3b5a9a;
    --snapa: #c13584;
    --pipline: #55acee;
  }
  * { box-sizing: border-box; margin: 0; padding: 0; }
  html, body { width: 1200px; height: 900px; overflow: hidden; }
  body { background: var(--backdrop); position: relative; font-family: "Roboto", Arial, sans-serif; }

  .card {
    position: absolute; width: 508px; height: 290px;
    background: var(--card-white); overflow: hidden;
    box-shadow: 0 4px 14px rgba(0,0,0,.45);
  }
  .card--owen { left: 64px; top: 160px; }
  .card--fiona { left: 628px; top: 160px; }
  .card--back { left: 353px; top: 519px; background: var(--brand-blue); }

  .brand { position: absolute; left: 28px; top: 48px; display: flex; align-items: center; gap: 8px; }
  .brand__dot { width: 40px; height: 40px; border-radius: 50%; background: var(--brand-blue); flex: none; }
  .brand__name { font-family: "Lato", Arial, sans-serif; font-weight: 700; font-size: 30px; color: var(--brand-blue); letter-spacing: -0.3px; }

  .person { position: absolute; right: 22px; top: 138px; text-align: right; }
  .person__name { font-family: "Lato", Arial, sans-serif; font-weight: 700; font-size: 19.5px; color: var(--brand-blue); line-height: 1; }
  .person__title { font-family: "Lato", Arial, sans-serif; font-size: 12px; color: var(--title-grey); margin-top: 12px; background: var(--card-white); padding-left: 7px; display: inline-block; position: relative; z-index: 1; }
  .divider { position: absolute; left: 22px; width: 464px; top: 171px; height: 1px; background: var(--brand-blue); }

  .contact { position: absolute; left: 22px; top: 204px; list-style: none; }
  .contact__item { display: flex; align-items: center; gap: 9px; font-size: 11px; font-weight: 300; color: var(--text-grey); height: 16px; }
  .contact__icon { width: 10px; height: 10px; flex: none; }

  .social { position: absolute; right: 22px; top: 233px; display: flex; gap: 6px; }
  .social__badge { width: 17px; height: 17px; border-radius: 50%; }
  .social__badge--chatterbook { background: var(--chatterbook); }
  .social__badge--snapa { background: var(--snapa); border-radius: 4px; }
  .social__badge--pipline { background: var(--pipline); }

  .wave { position: absolute; left: 0; bottom: 0; width: 508px; height: 27px; }

  .brand--back { left: 50%; top: 50%; transform: translate(-50%, -50%); gap: 12px; }
  .brand--back .brand__dot { width: 72px; height: 72px; background: var(--card-white); }
  .brand--back .brand__name { color: var(--card-white); font-size: 44px; }
</style>
</head>
<body>

<section class="card card--owen" aria-label="Business card front, Owen Radley">
  <div class="brand"><span class="brand__dot"></span><span class="brand__name">Brindle Offers</span></div>
  <div class="divider"></div>
  <div class="person">
    <div class="person__name">Owen Radley</div>
    <div class="person__title">Sales Director</div>
  </div>
  <ul class="contact">
    <li class="contact__item">
      <svg class="contact__icon" viewBox="0 0 10 10"><path d="M2 0.5 L3.6 2.6 L2.8 3.6 Q4 6 6.4 7.2 L7.4 6.4 L9.5 8 L8.3 9.5 Q3.5 9 0.5 1.7 Z" fill="var(--brand-blue)"/></svg>
      07912358046</li>
    <li class="contact__item">
      <svg class="contact__icon" viewBox="0 0 10 10"><rect x="0.5" y="2" width="9" height="6.5" fill="var(--brand-blue)"/><path d="M1 2.5 L5 5.6 L9 2.5" stroke="#fff" stroke-width="0.9" fill="none"/></svg>
      owen@brindleoffers.co.uk</li>
    <li class="contact__item">
      <svg class="contact__icon" viewBox="0 0 10 10"><circle cx="5" cy="5" r="4.5" fill="var(--brand-blue)"/><path d="M0.5 5 H9.5 M5 0.5 Q2.5 5 5 9.5 M5 0.5 Q7.5 5 5 9.5" stroke="#fff" stroke-width="0.7" fill="none"/></svg>
      www.brindleoffers.co.uk</li>
  </ul>
  <div class="social">
    <span class="social__badge social__badge--chatterbook" role="img" aria-label="Chatterbook"></span>
    <span class="social__badge social__badge--snapa" role="img" aria-label="Snapa"></span>
    <span class="social__badge social__badge--pipline" role="img" aria-label="Pipline"></span>
  </div>
  <svg class="wave" viewBox="0 0 508 27" preserveAspectRatio="none" aria-hidden="true">
    <rect x="0" y="5" width="275" height="6" fill="var(--brand-grey)"/>
    <path d="M0 14 H250 Q272 14 282 6 Q290 0 305 0 H508 V27 H0 Z" fill="var(--brand-blue)"/>
  </svg>
</section>

<section class="card card--fiona" aria-label="Business card front, Fiona Bracken">
  <div class="brand"><span class="brand__dot"></span><span class="brand__name">Brindle Offers</span></div>
  <div class="divider"></div>
  <div class="person">
    <div class="person__name">Fiona Bracken</div>
    <div class="person__title">Operations Director</div>
  </div>
  <ul class="contact">
    <li class="contact__item">
      <svg class="contact__icon" viewBox="0 0 10 10"><path d="M2 0.5 L3.6 2.6 L2.8 3.6 Q4 6 6.4 7.2 L7.4 6.4 L9.5 8 L8.3 9.5 Q3.5 9 0.5 1.7 Z" fill="var(--brand-blue)"/></svg>
      01632840275</li>
    <li class="contact__item">
      <svg class="contact__icon" viewBox="0 0 10 10"><rect x="0.5" y="2" width="9" height="6.5" fill="var(--brand-blue)"/><path d="M1 2.5 L5 5.6 L9 2.5" stroke="#fff" stroke-width="0.9" fill="none"/></svg>
      fiona@brindleoffers.co.uk</li>
    <li class="contact__item">
      <svg class="contact__icon" viewBox="0 0 10 10"><circle cx="5" cy="5" r="4.5" fill="var(--brand-blue)"/><path d="M0.5 5 H9.5 M5 0.5 Q2.5 5 5 9.5 M5 0.5 Q7.5 5 5 9.5" stroke="#fff" stroke-width="0.7" fill="none"/></svg>
      www.brindleoffers.co.uk</li>
  </ul>
  <div class="social">
    <span class="social__badge social__badge--chatterbook" role="img" aria-label="Chatterbook"></span>
    <span class="social__badge social__badge--snapa" role="img" aria-label="Snapa"></span>
    <span class="social__badge social__badge--pipline" role="img" aria-label="Pipline"></span>
  </div>
  <svg class="wave" viewBox="0 0 508 27" preserveAspectRatio="none" aria-hidden="true">
    <rect x="0" y="5" width="275" height="6" fill="var(--brand-grey)"/>
    <path d="M0 14 H250 Q272 14 282 6 Q290 0 305 0 H508 V27 H0 Z" fill="var(--brand-blue)"/>
  </svg>
</section>

<section class="card card--back" aria-label="Business card back">
  <div class="brand brand--back"><span class="brand__dot"></span><span class="brand__name">Brindle Offers</span></div>
</section>

</body>
</html>
```